Industrial Recycling

-We are a recycling company. this postcard will be sent to industrial businesses. The name of our company is Fernbrook Salvage Partners. We want these businesses to contact us so that we can purchase their recyclable materials from them. We want to target Scrap Metal, Cardboard, Plastic, Waste Paper, Food Waste, Bakery Waste, E-Waste, Solid Fill. I want the Headline to be- We have been recycling for over 100 years. Under or over the headline, I want the attached picture. My attached picture will be the dominant picture. I also want a couple of other pictures: some ideas are- baled cardboard, baled scrap metal, Money, loose recyclables. anything else that looks good to you! A tagline will be: Our specialty is recycling unique waste-streams. another tagline will be: If a waste can be recycled, we will find a use for it! Another tagline: All it takes is one call or email, and we will handle the rest. Please include the attached logo.- Please include the following contact info:
Phone number is 800-555-0147, email is ted@salvo522.com, website is salvo522.com.
Updates

Good Morning, We would like to make a couple more changes to the post card before we chose a design. We are sorry for such a late request. Please remove the tag lines; If a waste can be recycled, we will find a use for it! And: All it takes is one call or email, and we will handle the rest. Please replace these tag lines with: "Call or email to schedule your free waste audit" and please remember to list: “Scrap Metal, Cardboard, Plastic, Waste Paper, Food Waste, Bakery Waste, E-Waste, Solid Fill” as some of the recyclable material we are looking to buy.

Industry/Entity Type

Industrial

```html
<!DOCTYPE html>
<html lang="en">
<head>
<meta charset="utf-8">
<title>Fernbrook Salvage Partners Postcard</title>
<link href="https://fonts.googleapis.com/css2?family=Questrial&family=Arimo:ital,wght@0,400;0,700;1,700&display=swap" rel="stylesheet">
<style>
:root{
  --stage:#4a4a4a;
  --paper:#ffffff;
  --green:#6f9e56;
  --green-text:#6aa14c;
  --ink:#111111;
  --charcoal:#3f3f3f;
  --red:#e3262b;
  --rule:#b8b8b8;
  --photo-sepia:#a89a84;
}
*{margin:0;padding:0;box-sizing:border-box}
html,body{width:1200px;height:943px;overflow:hidden;background:var(--stage)}
.stage{position:relative;width:1200px;height:943px}
.card{position:absolute;left:278px;background:var(--paper);overflow:hidden;font-family:"Questrial",sans-serif}
.card--front{top:15px;width:695px;height:450px}
.card--back{top:482px;width:692px;height:448px}
.abs{position:absolute}
.brand{display:flex;align-items:center;gap:10px;font-family:"Questrial",sans-serif;color:var(--charcoal);font-size:21px;line-height:1}
.brand__mark{width:40px;height:40px;background:var(--green)}
.brand__name{width:190px}
.headline{color:var(--charcoal);font-weight:400;line-height:1;white-space:nowrap}
.headline__top{right:151px;top:30px;font-size:26px}
.headline__mid{left:307px;top:54px;font-size:24px}
.headline__mid strong{font-family:"Arimo",sans-serif;font-weight:700;font-size:24px}
.headline__num{left:547px;top:48px;font-style:italic;color:var(--green-text);font-size:48px}
.headline__years{right:28px;top:88px;font-size:30px}
.social{left:570px;top:22px;display:flex;gap:3px}
.social span{width:21px;height:21px;background:var(--green);display:block}
.hero-photo{left:29px;top:88px;width:354px;height:162px;border:3px solid var(--paper);background:linear-gradient(135deg,#c4b7a1,var(--photo-sepia) 60%,#7b6e5c);box-shadow:0 0 0 1px #ccc}
.specialty{right:33px;top:157px;text-align:right;color:var(--paper);line-height:1}
.specialty .l1{font-size:24px}
.specialty .l2{font-family:"Arimo",sans-serif;font-weight:700;font-size:39px;margin:5px 0 3px}
.specialty .l3{font-size:24px}
.materials{left:30px;top:262px;font-family:"Arimo",sans-serif;color:var(--ink)}
.materials h2{font-size:13.5px;font-style:italic;font-weight:700;line-height:1.1;text-transform:uppercase;width:360px}
.materials ul{list-style:none;display:flex;flex-wrap:wrap;width:370px;margin-top:5px;gap:4px 12px}
.materials li{color:var(--paper);font-size:12px;font-weight:700}
.materials li::before{content:"▪";color:var(--ink);margin-right:2px}
.cta{font-family:"Arimo",sans-serif;font-size:16px;line-height:1.1;color:var(--ink)}
.cta b{font-weight:700}
.cta .white{color:var(--paper)}
.circle{width:92px;height:92px;border-radius:50%;border:4px solid var(--paper);box-shadow:0 2px 4px rgba(0,0,0,.35)}
.footer{left:0;bottom:0;width:100%;height:72px;background:var(--ink)}
.phone{display:flex;align-items:center;gap:8px;font-family:"Arimo",sans-serif;font-weight:700;color:var(--green-text)}
.contact{color:var(--paper);font-size:19px;line-height:1.25}
.contact div{display:flex;align-items:center;gap:8px}
.back-address{left:340px;top:38px;font-family:"Arimo",sans-serif;font-size:13px;line-height:1.2;color:var(--ink);text-transform:uppercase}
.stamp{left:600px;top:30px;width:59px;height:68px;border:1px solid var(--rule);font-family:"Arimo",sans-serif;font-size:10px;color:#888;text-align:center;padding-top:14px;line-height:1.3}
.about{left:34px;top:100px;width:526px;color:var(--paper);font-size:15px;line-height:15.5px;text-align:justify}
.services{left:32px;top:185px;color:var(--paper)}
.services h3{font-size:21px;font-weight:700;font-family:"Arimo",sans-serif;margin-bottom:3px}
.services li{list-style:none;display:flex;align-items:center;gap:6px;font-size:16px;height:24px}
.services li::before{content:"";width:17px;height:17px;border-radius:3px;background:#7fb5d9;display:block}
.addr-line{left:483px;width:185px;height:1px;background:var(--rule)}
</style>
</head>
<body>
<main class="stage">

  <section class="card card--front">
    <svg class="abs" style="left:0;top:0" width="695" height="450" viewBox="0 0 695 450" aria-hidden="true">
      <path d="M0 160 C80 166 200 174 300 178 L300 186 C200 184 80 180 0 178 Z" fill="var(--ink)"/>
      <path d="M0 182 C120 178 250 172 390 160 C520 149 620 142 695 139 L695 378 L0 378 Z" fill="var(--green)"/>
      <path d="M380 156 C490 146 600 134 695 126 L695 139 C600 143 490 151 380 158 Z" fill="var(--ink)"/>
    </svg>

    <div class="brand abs" style="left:30px;top:30px">
      <span class="brand__mark"></span><span class="brand__name">Fernbrook Salvage Partners</span>
    </div>

    <div class="social abs" aria-hidden="true"><span></span><span></span><span></span></div>

    <h1 class="headline" aria-label="We have been recycling for over 100 years">
      <span class="headline__top abs">We have been</span>
      <span class="headline__mid abs"><strong>RECYCLING</strong> for over</span>
      <span class="headline__num abs">100</span>
      <span class="headline__years abs">years</span>
    </h1>

    <div class="hero-photo abs" role="img" aria-label="Vintage photograph of two workers beside an early recycling truck"></div>

    <div class="specialty abs">
      <div class="l1">Our Specialty Is</div>
      <div class="l2">RECYCLING</div>
      <div class="l3">Unique Waste-Streams</div>
    </div>

    <div class="materials abs">
      <h2>Some of the recyclable material we are looking to buy</h2>
      <ul>
        <li>Scrap Metal,</li><li>Cardboard,</li><li>Plastic,</li><li>Waste Paper,</li>
        <li>Food Waste,</li><li>Bakery Waste,</li><li>E-Waste,</li><li>Solid Fill etc</li>
      </ul>
    </div>

    <p class="cta abs" style="left:31px;top:340px"><b>CALL OR EMAIL</b> To Schedule Your<br><b class="white">FREE</b> Waste Audit</p>

    <div class="circle abs" style="left:393px;top:272px;background:linear-gradient(#a7b3bd,#2b2b2b)" role="img" aria-label="Bags of loose recyclables piled in a lot"></div>
    <div class="circle abs" style="left:484px;top:272px;background:linear-gradient(135deg,#d9dccb,#8d9a80)" role="img" aria-label="Spread of paper money"></div>
    <div class="circle abs" style="left:576px;top:270px;background:linear-gradient(#f4f4f4,#3e8a55)" role="img" aria-label="Green bin filled with food waste"></div>

    <div class="footer abs">
      <div class="phone abs" style="left:37px;top:12px;font-size:38px">
        <svg width="32" height="32" viewBox="0 0 32 32" aria-hidden="true"><circle cx="16" cy="16" r="14.5" fill="none" stroke="#fff" stroke-width="2"/><path d="M11 8l3 4-2 2c1 3 3 5 6 6l2-2 4 3-2 3c-7 0-14-7-14-14z" fill="#fff"/></svg>
        800 - 555-0147
      </div>
      <div class="contact abs" style="left:432px;top:8px">
        <div><svg width="17" height="17" viewBox="0 0 16 16" aria-hidden="true"><circle cx="8" cy="8" r="7" fill="none" stroke="#fff" stroke-width="1.5"/><path d="M1 8h14M8 1v14M3 4h10M3 12h10" stroke="#fff" stroke-width="1"/></svg>www.salvo522.com</div>
        <div><svg width="17" height="13" viewBox="0 0 17 13" aria-hidden="true"><rect x=".75" y=".75" width="15.5" height="11.5" fill="none" stroke="#fff" stroke-width="1.5"/><path d="M1 1l7.5 6L16 1" fill="none" stroke="#fff" stroke-width="1.5"/></svg>ted@salvo522.com</div>
      </div>
    </div>
  </section>

  <section class="card card--back">
    <svg class="abs" style="left:0;top:0" width="692" height="448" viewBox="0 0 692 448" aria-hidden="true">
      <path d="M0 88 H580 V226 H460 V286 H0 Z" fill="var(--green)"/>
      <path d="M0 286 H460 V388 H307 V448 H0 Z" fill="var(--ink)"/>
    </svg>

    <div class="brand abs" style="left:30px;top:32px">
      <span class="brand__mark"></span><span class="brand__name">Fernbrook Salvage Partners</span>
    </div>

    <p class="back-address abs">2217 Calloway St Riverton,<br>CA 92000</p>
    <div class="stamp abs">Place<br>Stamp<br>Here</div>

    <p class="about abs">Fernbrook Salvage Partners was started after we realized that the majority of companies in the industry were using misinformation and their own leverage to overcharge small and large businesses alike! We know that you are in business to support yourself and your family we want you to have as much going into your pocket as possible!</p>

    <div class="services abs">
      <h3>Our Services</h3>
      <ul>
        <li>Waste Efficiency Optimization</li>
        <li>Water Profitization</li>
        <li>Waste Management</li>
      </ul>
    </div>

    <p class="cta abs" style="left:32px;top:291px;color:var(--paper);font-size:17px"><b style="color:var(--green-text)">CALL OR EMAIL</b> To Schedule Your <b style="color:var(--red);font-size:21px">FREE</b><br>Waste Audit</p>
    <p class="abs" style="left:32px;top:342px;color:var(--paper);font-family:'Arimo',sans-serif;font-size:14px">CALL US TODAY</p>

    <div class="phone abs" style="left:32px;top:364px;font-size:24px">
      <svg width="17" height="17" viewBox="0 0 32 32" aria-hidden="true"><circle cx="16" cy="16" r="14.5" fill="none" stroke="#fff" stroke-width="2.5"/><path d="M11 8l3 4-2 2c1 3 3 5 6 6l2-2 4 3-2 3c-7 0-14-7-14-14z" fill="#fff"/></svg>
      800 - 555-0147
    </div>
    <div class="contact abs" style="left:34px;top:390px;font-size:19px;line-height:1.05">
      <div><svg width="14" height="14" viewBox="0 0 16 16" aria-hidden="true"><circle cx="8" cy="8" r="7" fill="none" stroke="#fff" stroke-width="1.5"/><path d="M1 8h14M8 1v14M3 4h10M3 12h10" stroke="#fff" stroke-width="1"/></svg>www.salvo522.com</div>
      <div><svg width="15" height="11" viewBox="0 0 17 13" aria-hidden="true"><rect x=".75" y=".75" width="15.5" height="11.5" fill="none" stroke="#fff" stroke-width="1.5"/><path d="M1 1l7.5 6L16 1" fill="none" stroke="#fff" stroke-width="1.5"/></svg>ted@salvo522.com</div>
    </div>

    <div class="addr-line abs" style="top:279px"></div>
    <div class="addr-line abs" style="top:316px"></div>
    <div class="addr-line abs" style="top:354px"></div>
  </section>

</main>
</body>
</html>
```